DEAN COLLOPY PROPERTY SERVICES

I want a business card that is clean and simple.
'Dean Collopy Property Services' is the title.
Somewhere on the card needs to be 'Carpentry, Tiling, painting and garden services'

On the back of card
PH 087 394 1526
email: deancollopypropertyservices@fernmail.net

I have attached a picture of my other business. I would like the font and design to be similar to the bathroom business.

Many thanks.

```html
<!DOCTYPE html>
<html lang="en">
<head>
<meta charset="utf-8">
<title>Dean Collopy Property Services – Business Card</title>
<link href="https://fonts.googleapis.com/css2?family=Montserrat:wght@300;400&family=Open+Sans:wght@400&display=swap" rel="stylesheet">
<style>
  :root {
    --ink: #231f20;
    --paper: #ffffff;
    --muted: #6d6e71;
    --rule: #4d4d4f;
    --bg-top: #ffffff;
    --bg-bottom: #a6a6a6;
  }
  * { box-sizing: border-box; margin: 0; padding: 0; }
  html, body { width: 1200px; height: 1200px; overflow: hidden; }
  body {
    background: linear-gradient(180deg, var(--bg-top) 0%, var(--bg-top) 25%, var(--bg-bottom) 100%);
    position: relative;
    font-family: "Open Sans", sans-serif;
  }
  .card {
    position: absolute;
    left: 240px;
    width: 720px;
    height: 411px;
    border-radius: 34px;
    overflow: hidden;
    box-shadow: 0 14px 30px rgba(0,0,0,0.18);
  }

  /* Front */
  .card--front { top: 120px; background: var(--ink); }
  .card--front .front-strip {
    position: absolute; left: 0; right: 0; bottom: 0; height: 52px;
    background: var(--paper);
  }
  .brand {
    position: absolute; left: 0; right: 0; top: 118px;
    text-align: center; color: var(--paper);
    font-family: "Montserrat", sans-serif; font-weight: 300;
  }
  .brand__name { font-size: 68px; letter-spacing: 1px; line-height: 1; }
  .brand__trade { font-size: 24px; letter-spacing: 12px; margin-top: 10px; padding-left: 12px; }
  .brand__company { font-size: 14px; letter-spacing: 1px; margin-top: 8px; }

  /* Back */
  .card--back { top: 640px; background: var(--paper); }
  .back-band-right {
    position: absolute; top: 0; right: 0; width: 48px; bottom: 0;
    background: var(--ink);
  }
  .back-band-bottom {
    position: absolute; left: 0; right: 0; bottom: 0; height: 34px;
    background: var(--ink);
  }
  .contact {
    position: absolute; left: 70px; top: 150px; width: 540px;
    color: var(--ink);
  }
  .contact__name { font-size: 40px; letter-spacing: 2px; line-height: 1.1; }
  .contact__role { font-size: 19px; color: var(--muted); margin-top: 2px; }
  .contact__rule { height: 1px; background: var(--rule); margin: 10px 0 10px 280px; }
  .contact__lines { font-size: 16px; line-height: 1.55; }
  .contact__lines .label { display: inline-block; width: 62px; color: var(--ink); }
  .contact__lines .value { color: var(--muted); }
  .contact__rule--full { height: 1px; background: var(--rule); margin: 10px 0 8px; }
  .contact__services { font-size: 17px; color: var(--muted); }
</style>
</head>
<body>

  <section class="card card--front" aria-label="Card front">
    <div class="brand">
      <div class="brand__name">Dean Collopy</div>
      <div class="brand__trade">BATHROOMS</div>
      <div class="brand__company">DEAN COLLOPY PROPERTY SERVICES</div>
    </div>
    <div class="front-strip"></div>
  </section>

  <section class="card card--back" aria-label="Card back">
    <div class="back-band-right"></div>
    <div class="back-band-bottom"></div>
    <div class="contact">
      <div class="contact__name">DEAN COLLOPY</div>
      <div class="contact__role">Owner</div>
      <div class="contact__rule"></div>
      <div class="contact__lines">
        <div><span class="label">Tel</span><span class="value">: 087 394 1526</span></div>
        <div><span class="label">Email</span><span class="value">: deancollopypropertyservices@fernmail.net</span></div>
      </div>
      <div class="contact__rule--full"></div>
      <div class="contact__services">Carpentry, Tiling, Painting And Garden Services</div>
    </div>
  </section>

</body>
</html>
```